Twitch Streamer Needs a Business Card Design

I need a business card design for my Twitch stream. It's a channel that plays a variety of games but has a modern royal theme with purple, black and gold as the main colors. Font should be easily readable but have a bit of flair to it to make it stand out/be unique. Should be a bit edgy and funky, but maintain the royal theme. Only standard shaped business cards please.
Updates

- Name on the card should read Wendel Pashby, not Duke Varlosk- Would like to see designs with and without Duke Varlosk on the back with the logo Added Sunday, February 22, 2015

Target Market(s)

Game Developers and product makers

Industry/Entity Type

Games

Contact Information for Business Card

I would like to have the logo on the back. Contact info I need on the card would be my phone number, Twitch, Social, email, and Channel.

Requirements
Must have
• Name: Duke Varlosk
• Phone Number: 401-555-0178
• Twitch: streamhall.tv/dukevarlosk
• Social: @DukeVarlosk
• Email: dukevarlosk@mailvexa.com
• Channel: Duke Varlosk
• Logo on the back
• "Duke Varlosk" below logo
Nice to have
• Font should be easily readable but have a small bit of unique flair.

```html
<!DOCTYPE html>
<html lang="en">
<head>
<meta charset="utf-8">
<title>Duke Varlosk – Business Card</title>
<link rel="stylesheet" href="https://fonts.googleapis.com/css2?family=Cormorant+Garamond:wght@500;600&family=Grenze+Gotisch:wght@400&family=Grenze:ital,wght@1,400&display=swap">
<style>
  :root {
    --backdrop: #3a2e25;
    --card: #ffffff;
    --card-shade: #f1f1f3;
    --purple: #6a2a8e;
    --purple-deep: #4e1a6c;
    --gold: #c9a93a;
    --gold-light: #e6cf6a;
  }
  * { margin: 0; padding: 0; box-sizing: border-box; }
  html, body {
    width: 1200px; height: 885px; overflow: hidden;
    background: var(--backdrop);
  }
  .stage {
    position: relative; width: 1200px; height: 885px;
    display: flex; align-items: center; justify-content: center; gap: 40px;
  }
  .card {
    position: relative; width: 540px; height: 309px;
    background: linear-gradient(160deg, var(--card) 55%, var(--card-shade));
    border-radius: 3px; overflow: hidden;
    box-shadow: 0 10px 28px rgba(0,0,0,.45);
  }
  .card__band { position: absolute; inset: 0; width: 100%; height: 100%; }
  .brand-mark {
    position: absolute; display: flex; align-items: center; gap: 10px;
    font-family: "Cormorant Garamond", serif; font-weight: 600;
    font-size: 30px; color: var(--purple); white-space: nowrap;
  }
  .brand-mark__square { width: 18px; height: 18px; background: var(--gold); }
  .card--back .brand-mark { left: 50%; top: 92px; transform: translateX(-50%); }
  .card__email {
    position: absolute; left: 0; right: 0; top: 268px; text-align: center;
    font-family: "Grenze", serif; font-style: italic; font-size: 19px;
    color: var(--gold-light); letter-spacing: .3px;
  }
  .card--front .brand-mark { right: 28px; top: 78px; font-size: 26px; }
  .contact {
    position: absolute; left: 96px; top: 136px; list-style: none;
    font-size: 17px; line-height: 24px;
  }
  .contact__label {
    font-family: "Grenze Gotisch", serif; color: var(--gold);
    display: inline-block; width: 82px;
  }
  .contact__value { font-family: "Cormorant Garamond", serif; font-weight: 600; color: var(--purple); }
  .card__name {
    position: absolute; left: 40px; top: 262px;
    font-family: "Grenze Gotisch", serif; font-size: 28px;
    color: var(--gold-light); letter-spacing: .5px;
  }
</style>
</head>
<body>
<main class="stage">
  <article class="card card--back">
    <svg class="card__band" viewBox="0 0 540 309" aria-hidden="true">
      <defs>
        <linearGradient id="bandBack" x1="0" y1="0" x2="1" y2="0">
          <stop offset="0" stop-color="#7b3aa0"/>
          <stop offset="1" stop-color="#4e1a6c"/>
        </linearGradient>
      </defs>
      <path d="M0,204 Q270,246 540,204" fill="none" stroke="#c9a93a" stroke-width="6"/>
      <path d="M0,216 Q270,258 540,216 L540,309 L0,309 Z" fill="url(#bandBack)"/>
    </svg>
    <div class="brand-mark"><span class="brand-mark__square"></span>Duke Varlosk</div>
    <p class="card__email">dukevarlosk@mailvexa.com</p>
  </article>

  <article class="card card--front">
    <svg class="card__band" viewBox="0 0 540 309" aria-hidden="true">
      <defs>
        <linearGradient id="bandFront" x1="0" y1="0" x2="1" y2="0">
          <stop offset="0" stop-color="#8a4bb0"/>
          <stop offset="1" stop-color="#5a2079"/>
        </linearGradient>
      </defs>
      <path d="M0,220 Q270,262 540,220" fill="none" stroke="#c9a93a" stroke-width="6"/>
      <path d="M0,232 Q270,274 540,232 L540,309 L0,309 Z" fill="url(#bandFront)"/>
    </svg>
    <div class="brand-mark"><span class="brand-mark__square"></span>Duke Varlosk</div>
    <ul class="contact">
      <li><span class="contact__label">Phone :</span><span class="contact__value">401-555-0178</span></li>
      <li><span class="contact__label">Social :</span><span class="contact__value">@DukeVarlosk</span></li>
      <li><span class="contact__label">Channel :</span><span class="contact__value">Duke Varlosk</span></li>
    </ul>
    <p class="card__name">Wendel Pashby</p>
  </article>
</main>
</body>
</html>
```